Creative - Appealing - Business Card Design Project

Looking for a Business card design (vector artwork) for an existing company called 'Copperfield Sound'. We operate in the entertainment industry specializing in audio system design and rental, however; we also deal with other sectors of the entertainment industry including lighting, video, staging and power system design and rental. We would like to see designs that don't focus too much on audio but include elements encompassing everything else.

Double sided business card, following our new colour scheme and logo, which is attached. The card would ideally be creative and eye catching to draw in new customers in the elegant event production market, such as weddings & corporate affairs.

Target Market(s)

High end corporate clients, wedding clients

Industry/Entity Type

Entertainment

Requirements
Must have
• Our contact details, these can be worded & listed however you think appropriate as part as the design

Business Name - Copperfield Sound
My Name - Benedict Thornbury
Web Address - www.copperfieldsound-example.com
Mobile Number - 07914 362 517
Office Number - 0330 411 7785
Email - ben@copperfieldsound-example.com

The name, email and mobile number would need to be able to be changed to my business partners also.

The font used on our logo is Sansation
Nice to have
• On one side maybe a word cloud involving the services in which we can provide; Lighting, Sound, Event Production, Staging, LED Uplighting, Projection Mapping, Wedding Hire

On the other side, all the important credentials of contact.
Should not have
• The design should not use any old style fonts (i.e Times New Roman, Gothic etc) or on the other side of the scale, any 'jokey' fonts (i.e. Comic Sans).

The font to be used is Sansation

```html
<!DOCTYPE html>
<html lang="en">
<head>
<meta charset="utf-8">
<title>Copperfield Sound – Business Card</title>
<link rel="stylesheet" href="https://fonts.googleapis.com/css2?family=Open+Sans:wght@400;600;700&display=swap">
<style>
  :root {
    --page-bg: #e9e9eb;
    --card-bg: #ffffff;
    --brand-purple: #5a2d8c;
    --accent-green: #8cc63f;
    --text-grey: #6d6e71;
    --rule-grey: #d4d4d6;
    --cloud-light: #ececee;
    --cloud-mid: #dcdcdf;
  }
  * { box-sizing: border-box; margin: 0; padding: 0; }
  html, body {
    width: 1200px; height: 1000px; overflow: hidden;
    background: var(--page-bg);
    font-family: "Open Sans", sans-serif;
  }
  .sheet {
    width: 1200px; height: 1000px;
    display: flex; flex-direction: column; align-items: center; justify-content: center;
    gap: 36px;
  }
  .card {
    position: relative;
    width: 700px; height: 453px;
    background: var(--card-bg);
    box-shadow: 0 2px 10px rgba(0,0,0,0.12);
    overflow: hidden;
  }
  .brand {
    position: absolute;
    display: flex; align-items: center; gap: 16px;
  }
  .brand-dot {
    width: 30px; height: 30px; border-radius: 50%;
    background: var(--brand-purple); flex: none;
  }
  .brand-name {
    font-weight: 700; color: var(--text-grey);
    text-transform: uppercase; line-height: 1.05; letter-spacing: 0.5px;
    white-space: nowrap;
  }
  .brand-name span { display: block; }

  /* Front: contact side */
  .card-front .brand { left: 48px; top: 250px; }
  .card-front .brand-name { font-size: 32px; }
  .card-front .divider {
    position: absolute; left: 330px; top: 38px; bottom: 38px;
    width: 1px; background: var(--rule-grey);
  }
  .contact { position: absolute; left: 360px; top: 96px; }
  .contact-name {
    font-weight: 700; font-size: 22px; color: var(--accent-green);
    margin-bottom: 30px; white-space: nowrap;
  }
  .contact-list { list-style: none; }
  .contact-list li {
    display: flex; align-items: center; gap: 10px;
    font-size: 14px; color: var(--text-grey);
    height: 28px; white-space: nowrap;
  }
  .contact-icon { width: 17px; height: 17px; flex: none; }

  /* Back: services word cloud side */
  .word-cloud {
    position: absolute; left: 360px; top: 28px; width: 320px;
    font-size: 20px; line-height: 36px; white-space: nowrap;
    color: var(--cloud-light);
  }
  .word-cloud b { font-weight: 700; color: var(--cloud-mid); }
  .card-back .brand { left: 48px; top: 170px; }
  .card-back .brand-name { font-size: 38px; }
  .card-back .web {
    position: absolute; left: 48px; bottom: 36px;
    font-size: 15px; font-weight: 700; color: var(--text-grey);
  }
</style>
</head>
<body>
<main class="sheet">

  <section class="card card-front" aria-label="Business card front">
    <div class="brand">
      <span class="brand-dot"></span>
      <span class="brand-name"><span>Copperfield</span><span>Sound</span></span>
    </div>
    <div class="divider"></div>
    <div class="contact">
      <p class="contact-name">Benedict Thornbury</p>
      <ul class="contact-list">
        <li>
          <svg class="contact-icon" viewBox="0 0 20 20"><circle cx="10" cy="10" r="9" fill="none" stroke="var(--brand-purple)" stroke-width="1.5"/><path d="M7 5.5l2 2-1 1.2c.6 1.3 1.6 2.3 2.9 2.9l1.2-1 2 2-1.2 1.5C9.6 13.8 6.2 10.4 5.9 7z" fill="var(--brand-purple)"/></svg>
          <span>0330 411 7785</span>
        </li>
        <li>
          <svg class="contact-icon" viewBox="0 0 20 20"><circle cx="10" cy="10" r="9" fill="none" stroke="var(--brand-purple)" stroke-width="1.5"/><rect x="7" y="4.5" width="6" height="11" rx="1" fill="none" stroke="var(--brand-purple)" stroke-width="1.4"/><circle cx="10" cy="13.3" r="0.8" fill="var(--brand-purple)"/></svg>
          <span>07914 362 517</span>
        </li>
        <li>
          <svg class="contact-icon" viewBox="0 0 20 20"><circle cx="10" cy="10" r="9" fill="none" stroke="var(--brand-purple)" stroke-width="1.5"/><rect x="5" y="6.5" width="10" height="7" fill="none" stroke="var(--brand-purple)" stroke-width="1.3"/><path d="M5 6.5l5 4 5-4" fill="none" stroke="var(--brand-purple)" stroke-width="1.3"/></svg>
          <span>ben@copperfieldsound-example.com</span>
        </li>
        <li>
          <svg class="contact-icon" viewBox="0 0 20 20"><circle cx="10" cy="10" r="9" fill="none" stroke="var(--brand-purple)" stroke-width="1.5"/><circle cx="10" cy="10" r="5" fill="none" stroke="var(--brand-purple)" stroke-width="1.2"/><path d="M5 10h10M10 5c-2 3-2 7 0 10M10 5c2 3 2 7 0 10" fill="none" stroke="var(--brand-purple)" stroke-width="1"/></svg>
          <span>www.copperfieldsound-example.com</span>
        </li>
      </ul>
    </div>
  </section>

  <section class="card card-back" aria-label="Business card back">
    <div class="word-cloud" aria-label="Services">
      <p>Wedding Hire <b>Projection</b> LED</p>
      <p><b>Sound</b> LED Uplighting <b>Staging</b></p>
      <p>Event Production <b>Lighting</b></p>
      <p><b>Projection Mapping</b> Sound</p>
      <p>Lighting <b>Event Production</b></p>
      <p><b>Sound</b> Staging Lighting</p>
      <p>Projection <b>Mapping</b> Event</p>
      <p>Wedding Hire <b>Sound</b> Staging</p>
      <p><b>Staging</b> LED Uplighting</p>
      <p>Event Production <b>Lighting</b></p>
      <p><b>Wedding Hire</b> Sound Event</p>
    </div>
    <div class="brand">
      <span class="brand-dot"></span>
      <span class="brand-name"><span>Copperfield</span><span>Sound</span></span>
    </div>
    <p class="web">www.copperfieldsound-example.com</p>
  </section>

</main>
</body>
</html>
```